Letterhead design for business

Looking for an attractive and professional letterhead that uses the logo that is attached below.

Target Market(s)

Potential bankruptcy clients.

Industry/Entity Type

Legal

Colors

Designer to choose colors to be used in the design.

Requirements
Must have
• Address for locations, phone number, and website address.
• Addresses are on website larkmoorfirm.legal. Use following phone number (for tracking purposes): 404-731-2864

```html
<!DOCTYPE html>
<html lang="en">
<head>
<meta charset="utf-8">
<title>Larkmoor Law Group — Letterhead</title>
<link href="https://fonts.googleapis.com/css2?family=Questrial&display=swap" rel="stylesheet">
<style>
  :root {
    --backdrop: #e6e4e0;
    --paper: #ffffff;
    --brand-green: #4ea75a;
    --brand-green-faint: #e4f1e5;
    --ink: #1c1c1c;
    --body-ink: #3a3a3a;
  }
  * { margin: 0; padding: 0; box-sizing: border-box; }
  html, body {
    width: 1200px; height: 801px; overflow: hidden;
    background: var(--backdrop);
    font-family: "Questrial", "Century Gothic", sans-serif;
  }
  .letterhead {
    position: absolute; left: 306px; top: 20px;
    width: 588px; height: 761px;
    background: var(--paper);
    box-shadow: 0 2px 10px rgba(0,0,0,.12);
    overflow: hidden;
  }
  .brand {
    position: absolute; left: 40px; top: 40px;
    display: flex; align-items: center; gap: 12px;
  }
  .brand-mark {
    width: 34px; height: 34px; border-radius: 50%;
    background: var(--brand-green);
  }
  .brand-text { display: flex; flex-direction: column; }
  .brand-name {
    font-size: 22px; color: var(--brand-green); line-height: 1;
  }
  .brand-attorney {
    font-size: 9px; color: var(--brand-green); margin-top: 4px;
    letter-spacing: .3px;
  }
  .watermark-disc {
    position: absolute; right: -40px; top: 390px;
    width: 220px; height: 220px; border-radius: 50%;
    background: var(--brand-green-faint);
  }
  .letter-body {
    position: absolute; left: 230px; top: 140px; width: 318px;
    font-size: 9.5px; line-height: 1.5; color: var(--body-ink);
  }
  .letter-body p { margin-bottom: 14px; }
  .contact-footer {
    position: absolute; left: 40px; bottom: 34px;
    display: flex; gap: 12px;
  }
  .footer-rule { width: 3px; background: var(--brand-green); }
  .contact-lines { font-size: 12px; line-height: 1.45; color: var(--ink); }
  .contact-lines .office { color: var(--brand-green); font-size: 10.5px; }
</style>
</head>
<body>
  <main class="letterhead">
    <header class="brand">
      <span class="brand-mark"></span>
      <div class="brand-text">
        <span class="brand-name">Larkmoor Law Group</span>
        <span class="brand-attorney">by Attorney M. Halvorsen</span>
      </div>
    </header>

    <div class="watermark-disc" aria-hidden="true"></div>

    <section class="letter-body">
      <p>Lorem ipsum dolor sit amet, consectetur adipiscing elit. Donec orci purus, luctus vitae dignissim eu, iaculis sed purus. Vivamus faucibus, ipsum nec aliquet viverra, leo mauris condimentum ligula, sit amet sagittis enim ligula quis arcu. Nam egestas tortor id nisi porttitor mattis. Phasellus nec eros mauris, et scelerisque orci.</p>
      <p>Donec rutrum mi, id feugiat ante nisi eu risus. Vestibulum nunc ornare, rhoncus a placerat in, ultricies in mi. Cras mattis varius eros, vel fringilla nisi suscipit eget. Quisque sagittis nulla at porttitor. Mauris a justo et tellus interdum tristique. Sed id augue vitae urna euismod commodo aliquet a quam.</p>
      <p>Integer laoreet faucibus ultricies. Morbi semper tincidunt gravida, sem arcu adipiscing lacus, ac bibendum nulla leo eu purus. Donec eu magna a metus ornare faucibus. Fusce aliquet faucibus lorem. Morbi semper, est id tincidunt gravida, nulla leo eu purus. Quisque nec diam sed risus consectetur a accumsan quis nibh.</p>
    </section>

    <footer class="contact-footer">
      <span class="footer-rule"></span>
      <div class="contact-lines">
        <div>(404) 731-2864</div>
        <div>info@larkmoorfirm.legal</div>
        <div>www.larkmoorfirm.legal</div>
        <div class="office">412 Tannery Row, Millbrook, Georgia 30871</div>
        <div class="office">275 Linden Hill Ave., NW Suite #1450 Fairhaven, Georgia 30519</div>
      </div>
    </footer>
  </main>
</body>
</html>
```